Business Cards

Business card design for my company.
I would like the card's background colour to be black. You can also see our web site to get an idea of our brand. https://www.dlqmarrowfield.com.au/
- Name
- Email

```html
<!DOCTYPE html>
<html lang="en">
<head>
<meta charset="utf-8">
<title>DLQ Marrowfield – Business Cards</title>
<link rel="stylesheet" href="https://fonts.googleapis.com/css2?family=Montserrat:wght@400;500;700&display=swap">
<style>
  :root {
    --stage: #3b3b3b;
    --card: #151515;
    --green: #179442;
    --white: #f4f4f4;
    --silver: #bdbdbd;
  }
  * { margin: 0; padding: 0; box-sizing: border-box; }
  html, body { width: 1200px; height: 689px; overflow: hidden; background: var(--stage); }
  body { font-family: "Montserrat", Arial, sans-serif; position: relative; }

  .card {
    position: absolute;
    top: 185px;
    width: 520px;
    height: 318px;
    background: var(--card);
    border-radius: 18px;
    overflow: hidden;
  }
  .card--front { left: 50px; }
  .card--back { left: 630px; }

  /* front */
  .front-brand {
    position: absolute;
    inset: 0;
    display: flex;
    align-items: center;
    justify-content: center;
    gap: 16px;
  }
  .front-brand__square { width: 26px; height: 26px; background: var(--silver); }
  .front-brand__name {
    font-weight: 700;
    font-size: 34px;
    letter-spacing: 3px;
    color: var(--silver);
  }

  /* back */
  .back-brand {
    position: absolute;
    left: 40px;
    top: 112px;
    display: flex;
    align-items: center;
    gap: 12px;
  }
  .back-brand__square { width: 18px; height: 18px; background: var(--green); }
  .back-brand__name {
    font-weight: 700;
    font-size: 24px;
    letter-spacing: 2px;
    color: var(--white);
    white-space: nowrap;
  }

  .person {
    position: absolute;
    right: 48px;
    top: 38px;
    text-align: right;
  }
  .person__name { font-weight: 700; font-size: 24px; line-height: 30px; color: var(--green); white-space: nowrap; }
  .person__role { font-weight: 500; font-size: 13px; line-height: 18px; color: var(--white); margin-top: 2px; white-space: nowrap; }
  .person-bar {
    position: absolute;
    right: 24px;
    top: 38px;
    width: 9px;
    height: 50px;
    background: var(--green);
  }

  .contacts {
    position: absolute;
    left: 40px;
    bottom: 32px;
    list-style: none;
    color: var(--white);
    font-size: 14px;
  }
  .contacts__item { display: flex; align-items: center; gap: 12px; height: 24px; white-space: nowrap; }
  .contacts__item--address { margin-bottom: 12px; }
  .contacts__icon { width: 14px; height: 14px; fill: var(--green); flex: none; }
</style>
</head>
<body>

  <section class="card card--front" aria-label="Card front">
    <div class="front-brand">
      <span class="front-brand__square"></span>
      <span class="front-brand__name">DLQ MARROWFIELD</span>
    </div>
  </section>

  <section class="card card--back" aria-label="Card back">
    <div class="person-bar"></div>
    <div class="person">
      <p class="person__name">Liam Corrigan</p>
      <p class="person__role">General Manager</p>
    </div>

    <div class="back-brand">
      <span class="back-brand__square"></span>
      <span class="back-brand__name">DLQ MARROWFIELD</span>
    </div>

    <ul class="contacts">
      <li class="contacts__item contacts__item--address">
        <svg class="contacts__icon" viewBox="0 0 24 24" aria-hidden="true"><path d="M12 1a8 8 0 0 0-8 8c0 6 8 14 8 14s8-8 8-14a8 8 0 0 0-8-8zm0 11a3 3 0 1 1 0-6 3 3 0 0 1 0 6z"/></svg>
        Eastbrook, Tasmania, Australia
      </li>
      <li class="contacts__item">
        <svg class="contacts__icon" viewBox="0 0 24 24" aria-hidden="true"><path d="M6.6 10.8a15 15 0 0 0 6.6 6.6l2.2-2.2a1 1 0 0 1 1-.25 11.4 11.4 0 0 0 3.6.57 1 1 0 0 1 1 1V20a1 1 0 0 1-1 1A17 17 0 0 1 3 4a1 1 0 0 1 1-1h3.5a1 1 0 0 1 1 1c0 1.25.2 2.45.57 3.6a1 1 0 0 1-.25 1z"/></svg>
        0400 555 182
      </li>
      <li class="contacts__item">
        <svg class="contacts__icon" viewBox="0 0 24 24" aria-hidden="true"><path d="M2 5h20v14H2zm2 2v.5l8 5 8-5V7l-8 5z"/></svg>
        info@dlqmarrowfield.com.au
      </li>
      <li class="contacts__item">
        <svg class="contacts__icon" viewBox="0 0 24 24" aria-hidden="true"><path d="M12 2a10 10 0 1 0 0 20 10 10 0 0 0 0-20zm6.9 6h-3a15 15 0 0 0-1.3-3.9A8 8 0 0 1 18.9 8zM12 4c.8 1.2 1.5 2.5 1.9 4h-3.8c.4-1.5 1.1-2.8 1.9-4zM4.3 14a8 8 0 0 1 0-4h3.4a16 16 0 0 0 0 4zm.8 2h3a15 15 0 0 0 1.3 3.9A8 8 0 0 1 5.1 16zm3-8h-3a8 8 0 0 1 4.3-3.9A15 15 0 0 0 8.1 8zM12 20c-.8-1.2-1.5-2.5-1.9-4h3.8c-.4 1.5-1.1 2.8-1.9 4zm2.3-6H9.7a14 14 0 0 1 0-4h4.6a14 14 0 0 1 0 4zm.3 5.9a15 15 0 0 0 1.3-3.9h3a8 8 0 0 1-4.3 3.9zm1.7-5.9a16 16 0 0 0 0-4h3.4a8 8 0 0 1 0 4z"/></svg>
        www.dlqmarrowfield.com.au
      </li>
    </ul>
  </section>

</body>
</html>
```